Quarnfield Fintech Product Infographic

Quarnfield is an established Fintech business, supplying complex financial software to banks and building societies.

We currently have a picture/infographic to show each of our 11 different software products in a single image. Each product can be installed on its own as a standalone application or if multiple products are installed they will share data.

The key message for our infographic is to convey the integration via a shared database.

The attached diagram is what we currently use which is to give you an idea of the message we are trying to give, but we are not tied to this format and are looking for this diagram to be reimagined.

We will look to use our new chosen design on printed media such as A4 Data sheets an example of which is attached.

For more information on our products please refer to www.quarnfield-example.co.uk/products

```html
<!DOCTYPE html>
<html lang="en">
<head>
<meta charset="utf-8">
<title>Quarnfield – Shared Data Product Suite</title>
<link href="https://fonts.googleapis.com/css2?family=Fira+Sans:wght@400;600;700&display=swap" rel="stylesheet">
<style>
  :root {
    --bg-top: #fafafa;
    --bg-bottom: #d8d8da;
    --green-light: #8dc63f;
    --green-dark: #39b54a;
    --magenta-dark: #9c1d89;
    --magenta-light: #d24d9b;
    --purple-dark: #453a8c;
    --purple-light: #6b58a4;
    --red-orange: #f15a24;
    --red: #ec1c24;
    --hub-ring: #c8ccd0;
    --hub-face: #f1f2f4;
    --hub-face-shade: #d6d9dd;
    --hub-text: #2c3e50;
    --icon-stroke: #6d6f73;
    --heading: #0d0d0d;
    --axis: #eadfe0;
  }
  html, body { margin: 0; padding: 0; overflow: hidden; }
  body {
    width: 874px; height: 1200px;
    background: linear-gradient(180deg, var(--bg-top) 0%, var(--bg-top) 65%, var(--bg-bottom) 100%);
  }
  .infographic { display: block; width: 874px; height: 1200px; }
  .product-label {
    font-family: "Fira Sans", Arial, sans-serif;
    font-weight: 600; font-size: 29px; fill: #fff; text-anchor: middle;
  }
  .group-heading {
    font-family: "Fira Sans", Arial, sans-serif;
    font-weight: 700; font-size: 35px; fill: var(--heading); text-anchor: middle;
  }
  .hub-shared {
    font-family: "Fira Sans", Arial, sans-serif;
    font-weight: 600; font-size: 36px; letter-spacing: 3px; fill: var(--hub-text); text-anchor: middle;
  }
  .hub-data {
    font-family: "Fira Sans", Arial, sans-serif;
    font-weight: 600; font-size: 36px; letter-spacing: 3px; fill: var(--hub-text); text-anchor: middle;
  }
  .icon-badge { fill: #f2f2f3; }
  .icon { fill: none; stroke: var(--icon-stroke); stroke-width: 2.6; stroke-linecap: round; stroke-linejoin: round; }
  .axis { stroke: var(--axis); stroke-width: 2; }
  .hub-ring { fill: var(--hub-ring); }
  .link-stem { fill: none; stroke: #9aa5ab; stroke-width: 3; }
  .node-open { fill: #fff; stroke: #9aa5ab; stroke-width: 4; }
  .node-green { fill: var(--green-dark); stroke: #9aa5ab; stroke-width: 4; }
  .node-magenta { fill: var(--magenta-light); stroke: #9aa5ab; stroke-width: 4; }
  .node-magenta-solid { fill: var(--magenta-dark); }
  .node-purple { fill: var(--purple-dark); stroke: #9aa5ab; stroke-width: 4; }
  .node-purple-solid { fill: var(--purple-dark); }
  .node-red { fill: var(--red); stroke: #9aa5ab; stroke-width: 4; }
  .node-red-solid { fill: var(--red); }
</style>
</head>
<body>
<svg class="infographic" viewBox="0 0 1652 2268" xmlns="http://www.w3.org/2000/svg" role="img" aria-label="Quarnfield products sharing one data hub">
  <defs>
    <rect id="diamond" x="-122" y="-122" width="244" height="244" rx="28" transform="rotate(45)"/>
    <linearGradient id="grad-green-lr" x1="0" x2="1" y1="0" y2="0">
      <stop offset="0" style="stop-color:var(--green-light)"/><stop offset="1" style="stop-color:var(--green-dark)"/>
    </linearGradient>
    <linearGradient id="grad-green-rl" x1="0" x2="1" y1="0" y2="0">
      <stop offset="0" style="stop-color:var(--green-dark)"/><stop offset="1" style="stop-color:var(--green-light)"/>
    </linearGradient>
    <linearGradient id="grad-magenta" x1="0" x2="1" y1="0" y2="0">
      <stop offset="0" style="stop-color:var(--magenta-dark)"/><stop offset="1" style="stop-color:var(--magenta-light)"/>
    </linearGradient>
    <linearGradient id="grad-purple" x1="0" x2="1" y1="0" y2="0">
      <stop offset="0" style="stop-color:var(--purple-dark)"/><stop offset="1" style="stop-color:var(--purple-light)"/>
    </linearGradient>
    <linearGradient id="grad-red" x1="0" x2="1" y1="0" y2="0">
      <stop offset="0" style="stop-color:var(--red-orange)"/><stop offset="1" style="stop-color:var(--red)"/>
    </linearGradient>
    <linearGradient id="grad-hub" x1="0" y1="0" x2="0" y2="1">
      <stop offset="0" style="stop-color:var(--hub-face-shade)"/><stop offset="0.5" style="stop-color:var(--hub-face)"/><stop offset="1" style="stop-color:#fbfbfc"/>
    </linearGradient>

    <g id="icon-dollar" class="icon">
      <path d="M12 -16 C8 -22 -12 -22 -12 -10 C-12 2 12 -2 12 10 C12 22 -8 22 -13 15"/>
      <path d="M0 -28 V-20 M0 20 V28"/>
    </g>
    <g id="icon-mail" class="icon">
      <rect x="-26" y="-17" width="52" height="34"/>
      <path d="M-26 -17 L0 4 L26 -17 M-26 17 L-7 -2 M26 17 L7 -2"/>
    </g>
    <g id="icon-doc" class="icon">
      <path d="M-18 -28 H12 L20 -20 V28 H-18 Z"/>
      <path d="M-10 -14 H12 M-10 -4 H12 M-10 6 H12 M-10 16 H12"/>
    </g>
    <g id="icon-house" class="icon">
      <path d="M-20 22 V-4 L0 -22 L20 -4 V22 Z"/>
      <path d="M-7 22 V6 H7 V22"/>
    </g>
    <g id="icon-signal" class="icon">
      <circle r="5"/>
      <path d="M-12 -10 A15 15 0 0 0 -12 10 M12 -10 A15 15 0 0 1 12 10"/>
      <path d="M-20 -17 A26 26 0 0 0 -20 17 M20 -17 A26 26 0 0 1 20 17"/>
      <path d="M-28 -24 A37 37 0 0 0 -28 24 M28 -24 A37 37 0 0 1 28 24"/>
    </g>
    <g id="icon-phone" class="icon">
      <rect x="-15" y="-30" width="30" height="60" rx="5"/>
      <path d="M-15 -21 H15 M-15 20 H15 M-4 -25 H4"/>
    </g>
    <g id="icon-card" class="icon">
      <rect x="-25" y="-17" width="50" height="34" rx="5"/>
      <path d="M-25 7 H25"/>
    </g>
  </defs>

  <!-- axes -->
  <line class="axis" x1="826" y1="663" x2="826" y2="1385"/>
  <line class="axis" x1="422" y1="971" x2="1236" y2="971"/>

  <!-- regulatory group -->
  <g class="product">
    <use href="#diamond" x="622" y="690" fill="url(#grad-green-rl)"/>
    <circle class="icon-badge" cx="622" cy="610" r="38"/>
    <use href="#icon-mail" x="622" y="610"/>
    <text class="product-label" x="622" y="710">Regulatory</text>
    <text class="product-label" x="624" y="743">Reporting</text>
  </g>
  <g class="product">
    <use href="#diamond" x="1029" y="684" fill="url(#grad-green-rl)"/>
    <circle class="icon-badge" cx="1029" cy="604" r="38"/>
    <use href="#icon-doc" x="1031" y="604"/>
    <text class="product-label" x="1029" y="704">Taxation</text>
    <text class="product-label" x="1033" y="737">Reporting</text>
  </g>
  <g class="product">
    <use href="#diamond" x="826" y="495" fill="url(#grad-green-lr)"/>
    <circle class="icon-badge" cx="826" cy="423" r="38"/>
    <use href="#icon-dollar" x="826" y="423"/>
    <text class="product-label" x="826" y="515">QDPS SCV</text>
  </g>
  <path class="link-stem" d="M705 548 V601 M945 548 V599"/>
  <circle class="node-open" cx="705" cy="601" r="12"/>
  <circle class="node-open" cx="945" cy="599" r="12"/>
  <circle class="node-green" cx="826" cy="663" r="12"/>

  <!-- performance group -->
  <g class="product">
    <use href="#diamond" x="254" y="969" fill="url(#grad-magenta)"/>
    <circle class="icon-badge" cx="254" cy="889" r="38"/>
    <use href="#icon-mail" x="254" y="889"/>
    <text class="product-label" x="256" y="988">Financial</text>
    <text class="product-label" x="256" y="1021">Planning</text>
  </g>
  <g class="product">
    <use href="#diamond" x="439" y="1169" fill="url(#grad-magenta)"/>
    <circle class="icon-badge" cx="439" cy="1089" r="38"/>
    <use href="#icon-house" x="439" y="1089"/>
    <text class="product-label" x="443" y="1199">Funds Transfer</text>
    <text class="product-label" x="447" y="1232">Pricing</text>
  </g>
  <g class="product">
    <use href="#diamond" x="636" y="1359" fill="url(#grad-magenta)"/>
    <circle class="icon-badge" cx="636" cy="1279" r="38"/>
    <use href="#icon-signal" x="636" y="1279"/>
    <text class="product-label" x="632" y="1385">Business</text>
    <text class="product-label" x="636" y="1418">Intelligence</text>
  </g>
  <circle class="node-magenta" cx="422" cy="971" r="12"/>
  <circle class="node-magenta-solid" cx="343" cy="1071" r="13"/>
  <circle class="node-magenta-solid" cx="544" cy="1258" r="13"/>

  <!-- finance group -->
  <g class="product">
    <use href="#diamond" x="1409" y="975" fill="url(#grad-purple)"/>
    <circle class="icon-badge" cx="1409" cy="895" r="38"/>
    <use href="#icon-doc" x="1411" y="895"/>
    <text class="product-label" x="1409" y="994">Financial</text>
    <text class="product-label" x="1413" y="1027">Ledgers</text>
  </g>
  <g class="product">
    <use href="#diamond" x="1214" y="1166" fill="url(#grad-purple)"/>
    <circle class="icon-badge" cx="1214" cy="1086" r="38"/>
    <use href="#icon-phone" x="1214" y="1086"/>
    <text class="product-label" x="1214" y="1196">Effective Interest</text>
    <text class="product-label" x="1218" y="1229">Rates</text>
  </g>
  <g class="product">
    <use href="#diamond" x="1016" y="1356" fill="url(#grad-purple)"/>
    <circle class="icon-badge" cx="1016" cy="1276" r="38"/>
    <use href="#icon-card" x="1016" y="1276"/>
    <text class="product-label" x="1014" y="1382">Hedge</text>
    <text class="product-label" x="1018" y="1415">Accounting</text>
  </g>
  <circle class="node-purple" cx="1236" cy="971" r="12"/>
  <circle class="node-purple-solid" cx="1299" cy="1058" r="13"/>
  <circle class="node-purple-solid" cx="1106" cy="1252" r="13"/>

  <!-- risk group -->
  <g class="product">
    <use href="#diamond" x="826" y="1547" fill="url(#grad-red)"/>
    <circle class="icon-badge" cx="826" cy="1467" r="38"/>
    <use href="#icon-dollar" x="826" y="1467"/>
    <text class="product-label" x="826" y="1579">Treasury</text>
  </g>
  <g class="product">
    <use href="#diamond" x="826" y="1898" fill="url(#grad-red)"/>
    <circle class="icon-badge" cx="826" cy="1818" r="38"/>
    <use href="#icon-dollar" x="826" y="1818"/>
    <text class="product-label" x="826" y="1944">ALM</text>
  </g>
  <circle class="node-red" cx="826" cy="1385" r="12"/>
  <circle class="node-red-solid" cx="826" cy="1722" r="14"/>

  <!-- hub -->
  <g class="hub">
    <circle class="hub-ring" cx="826" cy="983" r="138"/>
    <circle cx="834" cy="990" r="108" fill="#b9bdc2" opacity="0.6"/>
    <circle cx="826" cy="983" r="106" fill="url(#grad-hub)" stroke="#fff" stroke-width="3"/>
    <text class="hub-shared" x="828" y="988">SHARED</text>
    <text class="hub-data" x="829" y="1025">DATA</text>
  </g>

  <!-- group headings -->
  <text class="group-heading" x="830" y="798">REGULATORY</text>
  <text class="group-heading" x="559" y="960">PERFORMANCE</text>
  <text class="group-heading" x="1086" y="960">FINANCE</text>
  <text class="group-heading" x="825" y="1319">RISK</text>
</svg>
</body>
</html>
```